Marketing Brochure - Conjunction event

We need a brochure for clients/conjunction real estate agents to view the type of projects NESTA452 have available.
As a guideline of our requirements, please refer to our company profile. As you can see it is a simple elegant professional image we are after.
We are a Real Estate company specialise in off the plans project marketing. We have sale teams to sell the projects/ residential properties but also conjunction with other real estate agents. This is the first time we decided to use CraftHive to design our brochure. If pleasing results, ongoing we will have many more design projects to do.

Target Market(s)

Clients / real estate agents

Industry/Entity Type

Real Estate

Font styles to use
Sans Serif

Colors
ffffff
ef484e

Requirements
Must have
• All the details in the documents, Encourage creative designs.
• Company logo and the black banner as seen on company profile brochure
Nice to have
• similar to our company profile brochure( file attached)
Should not have
• Funky or too loud type image

```html
<!DOCTYPE html>
<html lang="en">
<head>
<meta charset="utf-8">
<title>NESTA452 Project Brochure</title>
<link rel="stylesheet" href="https://fonts.googleapis.com/css2?family=Archivo+Black&family=Lato:wght@400;700;900&display=swap">
<style>
  :root {
    --orange: #ef5a24;
    --red: #ef484e;
    --charcoal: #3a3b3f;
    --ink: #2b2b2b;
    --white: #ffffff;
    --backdrop: #e6e6e6;
    --frame: #2a2a2c;
  }
  * { box-sizing: border-box; margin: 0; padding: 0; }
  html, body { width: 1200px; height: 900px; overflow: hidden; }
  body {
    background: var(--backdrop);
    font-family: "Lato", sans-serif;
    color: var(--ink);
    position: relative;
  }
  .page {
    position: absolute;
    top: 55px;
    width: 540px;
    height: 790px;
    background: var(--white);
    overflow: hidden;
    box-shadow: 0 6px 18px rgba(0,0,0,.18);
  }
  .page--projects { left: 40px; }
  .page--cover { left: 620px; }

  .header-art { position: absolute; left: 0; top: 0; }

  .brand {
    position: absolute;
    display: flex;
    align-items: center;
    gap: 8px;
    font-weight: 900;
    color: var(--orange);
    letter-spacing: 1px;
  }
  .brand__dot {
    width: 18px; height: 18px;
    border-radius: 50%;
    background: var(--orange);
  }
  .page--projects .brand { left: 300px; top: 30px; font-size: 32px; }
  .page--cover .brand { left: 40px; top: 36px; font-size: 36px; }

  .project-grid {
    position: absolute;
    left: 22px; top: 170px;
    width: 496px;
    display: grid;
    grid-template-columns: 1fr 1fr;
    column-gap: 30px;
    row-gap: 22px;
  }
  .project { text-align: center; }
  .project__photo {
    width: 200px; height: 118px;
    margin: 0 auto 8px;
    border: 6px solid var(--frame);
    border-radius: 12px;
    box-shadow: 0 4px 8px rgba(0,0,0,.35);
  }
  .project__name {
    font-weight: 700;
    font-size: 17px;
    color: var(--orange);
    margin-bottom: 3px;
  }
  .project__meta {
    font-size: 9.5px;
    font-weight: 700;
    line-height: 1.35;
  }

  .photo--waterfront { background: linear-gradient(180deg, #8db4c9 0%, #dfe7ea 45%, #6f8a8f 100%); }
  .photo--facade { background: linear-gradient(160deg, #5b8fc7 0%, #cfd6dc 50%, #8a7760 100%); }
  .photo--street { background: linear-gradient(180deg, #6d87a8 0%, #b78f73 55%, #4a4438 100%); }
  .photo--tower { background: linear-gradient(180deg, #4f86c4 0%, #9bb27a 55%, #4a5a43 100%); }
  .photo--interior { background: linear-gradient(160deg, #3c3450 0%, #b05a6a 40%, #e8e2d8 75%, #6b5a48 100%); }
  .photo--garden { background: linear-gradient(180deg, #5d8fd0 0%, #9a7fc4 40%, #7ea062 70%, #b9b4a6 100%); }

  .cover-photo {
    position: absolute;
    left: 0; top: 120px;
    width: 540px; height: 670px;
    background: linear-gradient(115deg, #f4f4f4 0%, #d6d6d6 22%, #a9a9a9 38%, #e2e2e2 50%, #8c8c8c 64%, #3f3f3f 82%, #2e2e2e 100%);
  }
  .cover-inset {
    position: absolute;
    left: 330px; top: 130px;
    width: 180px; height: 150px;
    border-radius: 50%;
    border: 5px solid #d9d9d9;
    background: radial-gradient(circle at 50% 60%, #7d7d7d 0%, #c8c8c8 50%, #f0f0f0 100%);
    box-shadow: 0 3px 8px rgba(0,0,0,.3);
  }
  .mission {
    position: absolute;
    left: 0; top: 545px;
    width: 540px;
    padding: 12px 26px 16px;
    background: linear-gradient(90deg, rgba(255,255,255,.9) 0%, rgba(255,255,255,.78) 70%, rgba(255,255,255,.45) 100%);
  }
  .mission__title {
    font-family: "Archivo Black", sans-serif;
    font-size: 29px;
    color: var(--orange);
    line-height: 1.1;
    margin-bottom: 6px;
  }
  .mission__text {
    font-weight: 900;
    font-size: 15px;
    line-height: 1.3;
  }
</style>
</head>
<body>

  <section class="page page--projects">
    <svg class="header-art" width="540" height="180" viewBox="0 0 540 180" aria-hidden="true">
      <polygon points="0,0 540,0 540,120 0,160" fill="var(--orange)"/>
      <polygon points="250,0 540,0 540,92 270,112" fill="var(--charcoal)"/>
    </svg>
    <div class="brand"><span>NESTA452</span><span class="brand__dot"></span></div>

    <div class="project-grid">
      <article class="project">
        <div class="project__photo photo--waterfront" role="img" aria-label="Photo of a waterfront apartment complex"></div>
        <h3 class="project__name">Marlow | Rhodes</h3>
        <p class="project__meta">Location : 18 Harbourview Drive, Rhodes, NSW<br>Developer : Northgate/Kellan<br>Year : 2008</p>
      </article>
      <article class="project">
        <div class="project__photo photo--facade" role="img" aria-label="Photo of a modern glass apartment facade"></div>
        <h3 class="project__name">Fernleigh | Chippendale</h3>
        <p class="project__meta">Location : 27-35 Lane Street, Chippendale, NSW 2008<br>Developer : Verano<br>Year : 2013</p>
      </article>
      <article class="project">
        <div class="project__photo photo--street" role="img" aria-label="Photo of an apartment building on a street corner"></div>
        <h3 class="project__name">The Aldous | Canterbury</h3>
        <p class="project__meta">Location : 4B Elm Street, Canterbury, NSW 2193<br>Developer : Altrove<br>Year : 2014</p>
      </article>
      <article class="project">
        <div class="project__photo photo--tower" role="img" aria-label="Photo of a green-accented apartment tower"></div>
        <h3 class="project__name">Cedar Grove | Kogarah</h3>
        <p class="project__meta">Location : 40-52 Rowan Road, Kogarah, NSW 2217<br>Developer : Altrove<br>Year : 2014</p>
      </article>
      <article class="project">
        <div class="project__photo photo--interior" role="img" aria-label="Photo of a furnished apartment living room"></div>
        <h3 class="project__name">Linea Apartment | Redfern</h3>
        <p class="project__meta">Location : 11-13 Tamar Street, Redfern, NSW 2016<br>Developer : Altrove<br>Year : 2014</p>
      </article>
      <article class="project">
        <div class="project__photo photo--garden" role="img" aria-label="Photo of apartments behind flowering trees"></div>
        <h3 class="project__name">Wattle Estate stage I, II | Ryde</h3>
        <p class="project__meta">Location : 11-13 Tamar Street, Redfern, NSW 2016<br>Developer : Altrove<br>Year : 2014</p>
      </article>
    </div>
  </section>

  <section class="page page--cover">
    <div class="cover-photo" role="img" aria-label="Black and white photo of a tall modern apartment building with balconies, a tree and a street below"></div>
    <svg class="header-art" width="540" height="180" viewBox="0 0 540 180" aria-hidden="true">
      <polygon points="0,0 540,0 540,118 0,150" fill="var(--charcoal)"/>
      <polygon points="0,150 540,118 540,140 0,172" fill="var(--orange)"/>
    </svg>
    <div class="brand"><span>NESTA452</span><span class="brand__dot"></span></div>
    <div class="cover-inset" role="img" aria-label="Circular photo of an apartment terrace with a glass planter"></div>

    <div class="mission">
      <h2 class="mission__title">Mission Statement</h2>
      <p class="mission__text">Striving for excellence in the real estate sector, we aim to provide world class real estate services to the people of Sydney and overseas, embracing the highest standards of expertise, professionalism and integrity.</p>
    </div>
  </section>

</body>
</html>
```